Weight Loss Flyer

We are looking to get a flyer designed for our home consultant weight loss business. We call to customers homes and sell our meal replacement shakes, soups and bars and give nutrition and diet advice. We are mobile weight loss consultants. Our company is "The Slim Path Circle". We provide a free initial consultation which usually costs €30. We want the flyer to draw attention to our service and to contact us to help them lose weight.
We need an A4, A5, DL size flyers
Target Market(s)
Target audience is females between 30-60 years who want to lose weight and may have tried trim trackers, molly brandt etc...
Industry/Entity Type
Nutrition
Look and feel

```html
<!DOCTYPE html>
<html lang="en">
<head>
<meta charset="utf-8">
<title>The Slim Path Circle – Flyer</title>
<link href="https://fonts.googleapis.com/css2?family=Open+Sans:wght@600;700&family=Tinos:wght@400;700&display=swap" rel="stylesheet">
<style>
  :root {
    --green-dark: #1d6a1c;
    --green: #3a9a1f;
    --green-bright: #66bb1e;
    --green-text: #2c7a1c;
    --cream: #fdf5c6;
    --cream-light: #fffcea;
    --orange: #f7a21b;
    --orange-light: #fcc94a;
    --sky: #4f9de0;
    --sky-light: #cfe6f8;
    --field: #c7c826;
    --white: #ffffff;
    --ink: #222222;
  }
  * { box-sizing: border-box; margin: 0; padding: 0; }
  html, body { width: 849px; height: 1200px; overflow: hidden; }
  body { background: #ffffff; }
  .flyer {
    position: relative;
    width: 849px;
    height: 1200px;
    overflow: hidden;
    background: linear-gradient(180deg, var(--cream) 0%, var(--cream) 35%, var(--cream-light) 65%, var(--cream) 100%);
    font-family: "Tinos", "Times New Roman", serif;
  }
  .hero-photo {
    position: absolute; left: 0; top: 0; width: 849px; height: 380px;
    background: linear-gradient(180deg, var(--sky) 0%, var(--sky-light) 45%, #e9eb7a 62%, var(--field) 80%, #8fa820 100%);
  }
  .hero-wave { position: absolute; left: 0; top: 290px; width: 849px; height: 120px; }
  .brand-name {
    position: absolute; left: 30px; top: 40px; width: 400px;
    font-family: "Open Sans", Arial, sans-serif; font-weight: 700;
    font-size: 62px; line-height: 1.02; color: var(--green-dark);
    text-transform: uppercase;
  }
  .offer-badge {
    position: absolute; left: 36px; top: 375px; width: 178px; height: 178px;
    border-radius: 50%;
    background: radial-gradient(circle at 40% 35%, var(--orange-light), var(--orange) 70%);
    display: flex; align-items: center; justify-content: center;
  }
  .offer-badge span {
    display: block; transform: rotate(-28deg);
    color: var(--green-dark); font-weight: 700; font-size: 27px;
    line-height: 1.05; text-align: center; text-transform: uppercase;
  }
  .offer-pill {
    position: absolute; left: 254px; top: 419px; width: 568px; height: 87px;
    border-radius: 14px;
    background: linear-gradient(180deg, var(--green-bright), var(--green));
    color: var(--white); font-family: "Open Sans", Arial, sans-serif; font-weight: 700;
    font-size: 17.5px; line-height: 1.45; text-align: center;
    display: flex; align-items: center; justify-content: center; padding: 0 14px;
  }
  .intro {
    position: absolute; left: 24px; top: 584px; width: 420px;
    color: var(--green-text); font-size: 16.8px; line-height: 22.3px;
  }
  .intro p + p { margin-top: 22.3px; }
  .call-box {
    position: absolute; left: 21px; top: 922px; width: 403px; height: 134px;
    border-radius: 12px;
    background: linear-gradient(180deg, var(--green-bright), #4aa318);
    color: var(--white); font-weight: 700; font-size: 21px; line-height: 1.5;
    text-align: center; text-transform: uppercase;
    display: flex; align-items: center; justify-content: center;
  }
  .diet-card {
    position: absolute; left: 467px; top: 580px; width: 359px; height: 476px;
    border: 2px solid var(--green-bright); border-radius: 6px; background: var(--white);
    overflow: hidden;
  }
  .diet-card__header {
    height: 72px; background: linear-gradient(180deg, var(--green), var(--green-dark));
    color: var(--white); font-weight: 400; font-size: 42px; text-align: center; line-height: 72px;
    letter-spacing: 1px;
  }
  .diet-card__image {
    position: absolute; left: 90px; top: 290px; width: 250px; height: 180px;
    border-radius: 50%;
    background: radial-gradient(ellipse at center, rgba(240,160,80,0.35), rgba(150,200,90,0.25) 55%, rgba(255,255,255,0) 75%);
  }
  .diet-list { position: relative; padding: 22px 20px 0 22px; }
  .meal + .meal { margin-top: 20px; }
  .meal h3 { font-weight: 400; font-size: 25px; color: var(--green-dark); line-height: 30px; }
  .meal p { font-size: 17px; color: var(--ink); line-height: 21px; }
  .footer {
    position: absolute; left: 0; top: 1104px; width: 849px; height: 96px;
    background: linear-gradient(180deg, var(--green), var(--green-dark));
    border-top-left-radius: 20px; border-top-right-radius: 20px;
    color: var(--white); text-align: center;
  }
  .footer__label { font-size: 16.5px; padding-top: 9px; letter-spacing: 0.3px; }
  .footer__phone {
    font-family: "Open Sans", Arial, sans-serif; font-weight: 700; font-size: 40px; line-height: 1.3;
  }
</style>
</head>
<body>
<main class="flyer">
  <div class="hero-photo" role="img" aria-label="Photo of a fit smiling couple holding bathroom scales in a field of yellow flowers under a blue sky"></div>
  <svg class="hero-wave" viewBox="0 0 849 120" preserveAspectRatio="none" aria-hidden="true">
    <path d="M0 20 C220 80 520 40 849 35 L849 120 L0 120 Z" fill="#3a9a1f"/>
    <path d="M0 45 C240 95 540 55 849 48 L849 120 L0 120 Z" fill="#fcd63a"/>
    <path d="M0 55 C250 105 550 68 849 62 L849 120 L0 120 Z" fill="#fdf5c6"/>
  </svg>

  <h1 class="brand-name">The Slim Path Circle</h1>

  <div class="offer-badge"><span>Exclusive<br>Offer</span></div>

  <div class="offer-pill">Receive a FREE initial weight loss consultation at home worth €30 and make the change to a healthier, happier new you.</div>

  <section class="intro">
    <p>The Slim Path Circle are professionally trained Consultants who provide weekly one on one support, combined with a personalised and easy to follow weight loss solution - All in the convenience of your home, workplace or a location that suits you.</p>
    <p>Yes we are mobile - We come to you!</p>
    <p>The Slim Path Circle use a great tasting range of healthy meal options, meal replacement shakes and soup, low calorie snack and portion controlled meals. As well as fantastic personal one-on-one support from your Consultant, you will also gain access to your very own personalised 24 hour online support.</p>
  </section>

  <div class="call-box">Make the call today and the<br>Slim Path Circle<br>can start with you today!</div>

  <section class="diet-card">
    <h2 class="diet-card__header">DAILY DIET</h2>
    <div class="diet-card__image" role="img" aria-label="Faint photo of fresh fruit and vegetables"></div>
    <div class="diet-list">
      <div class="meal"><h3>Breakfast</h3><p>One Meal Replacement Shake</p></div>
      <div class="meal"><h3>Lunch</h3><p>One Meal Replacement Shake or Soup</p></div>
      <div class="meal"><h3>Dinner</h3><p>One piece of grilled steak or steamed fish and salad alternated with one of our healthy option meals</p></div>
      <div class="meal"><h3>Snack</h3><p>A serving of low fat yogurt or a piece of fruit or a snack from our list</p></div>
    </div>
  </section>

  <footer class="footer">
    <p class="footer__label">THE SLIM PATH CIRCLE CUSTOMER CARE INFO LINE</p>
    <p class="footer__phone">Call us 021 555 0147</p>
  </footer>
</main>
</body>
</html>
```